Funeral Services Site

We need a website for a Funeral Services company. The old website is: www.rouwcentrumdelvoort.be We need the same structure and text.

Target Market(s)

Customers.

Coding

Coded - Design and coding required

Number of Pages Required

4 page

Font styles to use
Serif
Sans Serif
Script

```html
<!DOCTYPE html>
<html lang="en">
<head>
<meta charset="utf-8">
<title>Funeral Home Delvoort bvba</title>
<link href="https://fonts.googleapis.com/css2?family=Nunito+Sans:wght@400;600;700;800&family=Lato:wght@400;700&display=swap" rel="stylesheet">
<style>
:root{
  --gold:#8c7455;
  --gold-soft:#a08763;
  --ink:#222;
  --text:#333;
  --black:#050505;
  --band:#393939;
  --bar:#2f2f2f;
  --white:#fff;
}
*{box-sizing:border-box;margin:0;padding:0}
html,body{width:826px;height:1200px;overflow:hidden;background:var(--white)}
body{position:relative;font-family:"Lato",sans-serif;color:var(--text)}
.abs{position:absolute}

/* header */
.site-header{left:0;top:0;width:826px;height:47px;background:var(--white);z-index:5}
.brand{left:172px;top:7px;display:flex;align-items:center;gap:8px}
.brand-mark{width:32px;height:32px;border-radius:50%;background:var(--ink)}
.brand-name{font-family:"Nunito Sans",sans-serif;font-weight:700;font-size:15px;line-height:15px;color:var(--ink);width:110px}
.header-phone{left:600px;top:11px;font-size:8px;color:var(--gold);display:flex;align-items:center;gap:4px}
.main-nav{left:405px;top:32px;display:flex;gap:19px;font-size:7.5px;color:var(--ink)}

/* hero */
.hero{left:0;top:47px;width:826px;height:388px;background:linear-gradient(100deg,#1f2226 0%,#3b3e42 30%,#6b6a68 55%,#8e8a84 70%,#4a4a48 100%)}
.hero-box{left:171px;top:103px;width:286px;height:159px;background:rgba(40,40,40,.72);border-radius:10px;padding:18px 20px;color:var(--white);font-family:"Nunito Sans",sans-serif}
.hero-kicker{font-size:15px;font-weight:800;white-space:nowrap}
.hero-title{font-size:22px;font-weight:800;line-height:30px;margin-top:6px;white-space:nowrap;letter-spacing:-.2px}
.btn{position:absolute;height:25px;border-radius:13px;font-size:7.5px;display:flex;align-items:center;justify-content:center;font-family:"Lato",sans-serif}
.btn-solid{background:var(--white);color:var(--ink)}
.btn-outline{border:2px solid var(--white);color:var(--white)}
.slider-dots{left:395px;top:340px;display:flex;gap:6px}
.slider-dots span{width:8px;height:8px;border-radius:50%;border:1.3px solid var(--white)}
.slider-dots .on{background:var(--white)}
.hero-curve{left:0;top:370px;width:826px;height:66px}

/* about */
.about{left:0;top:397px;width:826px;text-align:center}
.section-title{font-family:"Nunito Sans",sans-serif;font-weight:400;font-size:18px;color:var(--gold);letter-spacing:.5px}
.title-rule{width:24px;height:2px;background:var(--gold);margin:3px auto 0}
.about-lead{margin-top:14px;font-weight:700;font-size:10px;color:var(--gold)}
.about-text{font-size:7px;line-height:9px;color:var(--ink);margin:8px auto 0;width:490px}
.about-text.wide{width:490px;margin-top:9px}
.about-text b{color:var(--gold);font-weight:700}
.about-shadow{left:178px;top:515px;width:470px;height:8px;border-radius:50%;box-shadow:0 3px 4px -2px rgba(0,0,0,.35)}

/* worship */
.worship{left:0;top:547px;width:826px;height:226px;background:var(--black);color:var(--white)}
.worship-title{position:absolute;left:0;width:826px;top:20px;text-align:center;font-family:"Nunito Sans",sans-serif;font-weight:400;font-size:16.5px;letter-spacing:.3px}
.bouquet{left:55px;top:28px;width:260px;height:182px;border-radius:45%;background:radial-gradient(circle at 50% 50%,#c94a4a 0%,#e8b6b0 30%,#3d5a3a 60%,rgba(5,5,5,0) 72%)}
.orchid{left:650px;top:0;width:176px;height:200px;background:radial-gradient(circle at 60% 45%,#4a2a45 0%,#2a1728 40%,rgba(5,5,5,0) 72%)}
.worship-copy{left:345px;top:58px;width:310px;font-size:7px;line-height:9px;text-transform:uppercase}
.worship-copy p+p{margin-top:9px}
.worship-list{list-style:none;margin-top:9px}
.worship-list li{position:relative;padding-left:22px;font-size:6px;margin-bottom:8px}
.worship-list li::before{content:"";position:absolute;left:9px;top:1px;width:6px;height:6px;border-radius:50%;background:var(--white)}

/* service cards */
.card{top:798px;width:190px;height:130px;border-radius:18px 0 18px 0;color:var(--white);text-align:center;font-family:"Nunito Sans",sans-serif;padding-top:11px;overflow:hidden}
.card-condole{left:191px;background:linear-gradient(160deg,#3a3a3a,#1c1c1c)}
.card-flower{left:439px;background:linear-gradient(160deg,#4a4c4a,#2a2a2a 60%,#5a2a2e)}
.card-title{font-size:16px;font-weight:600}
.card-text{font-size:10px;line-height:12.5px;margin-top:8px}
.card .btn{left:37px;top:92px;width:116px;height:24px}

/* contact band */
.cta{left:0;top:954px;width:826px;height:130px;background:radial-gradient(ellipse at 20% 60%,#5a4c3c 0%,var(--band) 35%),var(--band)}
.cta-text{position:absolute;left:189px;top:22px;font-family:"Nunito Sans",sans-serif;font-weight:700;font-size:14.5px;line-height:17.5px;color:var(--white);white-space:nowrap}

/* footer */
.footer-brand{left:207px;top:1108px;display:flex;align-items:center;gap:12px}
.footer-brand .brand-mark{width:52px;height:52px}
.footer-brand .brand-name{font-size:22px;line-height:24px;width:150px}
.footer-divider{left:446px;top:1113px;width:1px;height:45px;background:#bbb}
.footer-contact{left:478px;top:1111px;color:var(--black);font-size:7px;line-height:8.5px}
.footer-contact .label{font-weight:700}
.footer-contact .number{font-size:16px;line-height:19px}
.bottom-bar{left:0;top:1182px;width:826px;height:18px;background:var(--bar);color:var(--white);font-size:5px;padding:6px 0 0 171px}
</style>
</head>
<body>

<header class="abs site-header">
  <div class="abs brand"><span class="brand-mark"></span><span class="brand-name">Funeral Home Delvoort</span></div>
  <div class="abs header-phone">
    <svg width="8" height="8" viewBox="0 0 24 24"><path fill="#8c7455" d="M6.6 10.8a15 15 0 006.6 6.6l2.2-2.2a1 1 0 011-.25 11.4 11.4 0 003.6.57 1 1 0 011 1V20a1 1 0 01-1 1A17 17 0 013 4a1 1 0 011-1h3.5a1 1 0 011 1c0 1.25.2 2.45.57 3.57a1 1 0 01-.25 1z"/></svg>
    012 34 56 78
  </div>
  <nav class="abs main-nav"><span>Home</span><span>About Us</span><span>Condole Online</span><span>Order Flowers</span><span>Contact</span></nav>
</header>

<section class="abs hero" role="img" aria-label="Cemetery with a stone flower basket holding a candle on a grave"></section>
<div class="abs hero-box">
  <div class="hero-kicker">Funeral Home Delvoort bvba:</div>
  <div class="hero-title">a Personal Service<br>in Farewell Guidance</div>
</div>
<div class="btn btn-solid" style="left:192px;top:220px;width:117px">012 34 56 78</div>
<div class="btn btn-outline" style="left:321px;top:220px;width:116px">CONTACT US</div>
<div class="abs slider-dots"><span></span><span class="on"></span><span></span></div>
<svg class="abs hero-curve" viewBox="0 0 826 66" preserveAspectRatio="none">
  <path d="M0 62 Q413 -10 826 58 L826 66 L0 66 Z" fill="#fff"/>
  <path d="M0 62 Q413 -10 826 58" fill="none" stroke="#8c7455" stroke-width="3"/>
</svg>

<section class="abs about">
  <h2 class="section-title">ABOUT US</h2>
  <div class="title-rule"></div>
  <p class="about-lead">Mourning center Delvoort, a complete service in mourning and farewell guidance</p>
  <p class="about-text">Saying goodbye to a loved one is one of the toughest things in a lifetime. Funeral home Delvoort in Riemst takes care of <b>all the practical and administrative matters</b> involved. So you can say goodbye in peace.</p>
  <p class="about-text wide">Our people have a <b>ruime experience in farewell guidance</b> and stand <b>for 24 hours at 24 hours</b> for you. Our fully renovated funeral home is open to you and your acquaintances, so that you can greet your loved one at any time of the day.</p>
</section>
<div class="abs about-shadow"></div>

<section class="abs worship">
  <div class="abs orchid" role="img" aria-label="Dark purple orchid flowers"></div>
  <div class="abs bouquet" role="img" aria-label="Bouquet of red, pink and white roses"></div>
  <h2 class="worship-title">ORGANIZATION FUNERAL AND WORSHIP</h2>
  <div class="abs worship-copy">
    <p>The organization of the funeral ceremony is a moment of reflection, where the personality of the deceased can be beautifully highlighted. Our team will assist you in this and select the most beautiful texts, songs and photos with you in order to arrive at an appropriate and worthy goodbye.</p>
    <p>The funeral can take place in your parish church or our auditorium if you wish, which can accommodate a maximum of 100 guests.<br>We can arrange the following for you:</p>
    <ul class="worship-list">
      <li>Vigil the night before the funeral</li>
      <li>Prayer service with priest (if possible)</li>
      <li>Eucharistic celebration with priest (on Tuesday and Friday in the parishes of Riemst)</li>
    </ul>
  </div>
</section>

<div class="abs card card-condole" role="img" aria-label="Dim photo of a stone angel statue">
  <div class="card-title">CONDOLE ONLINE</div>
  <div class="card-text">DO YOU WANT TO LEAVE<br>NICE WORDS TO THE FAMILY<br>OF A DECEASED PERSON?</div>
  <div class="btn btn-solid">SEND NOW</div>
</div>
<div class="abs card card-flower" role="img" aria-label="Dim photo of graves with red flowers">
  <div class="card-title">RESERVE FLOWER</div>
  <div class="card-text">THERE IS ALWAYS AN<br>ENGAGING SELECTION OF<br>FLORAL ARRANGEMENTS</div>
  <div class="btn btn-outline">RESERVE</div>
</div>

<section class="abs cta" role="img" aria-label="Dark photo of a candle and an orange flower">
  <p class="cta-text">DO YOU HAVE ANY QUESTIONS OR WOULD YOU LIKE TO CALL<br>IN OUR FUNERAL HOME? CONTACT US. WE ARE HERE FOR YOU.</p>
  <div class="btn btn-solid" style="left:291px;top:80px;width:116px">012 34 56 78</div>
  <div class="btn btn-outline" style="left:419px;top:80px;width:116px">CONTACT US</div>
</section>

<footer>
  <div class="abs footer-brand"><span class="brand-mark"></span><span class="brand-name">Funeral Home Delvoort</span></div>
  <div class="abs footer-divider"></div>
  <div class="abs footer-contact">
    <div class="label">Call Us:</div>
    <div class="number">012 34 56 78</div>
    <div>Lindenweg 14, 3770 Riemst</div>
    <div><span class="label">Email:</span> info@rouwcentrumdelvoort.be</div>
  </div>
  <div class="abs bottom-bar">© Copy Right 2019. All Right Reserved.</div>
</footer>

</body>
</html>
```